Business Card Design

We need a business card designed for our new company. Prefer a black card with white logo & writing.

Contact Information for Business Card

Dale Pickett, address: 7-4417 Larchmere Avenue, Abbotsford, BC, V3K 2R9, Office Phone: 604-555-0172, Cell: 604-555-0138, Email: dale@kelsoncoatworks.ca

Colors

Designer to choose only greyscale colors for use in the design.

```html
<!DOCTYPE html>
<html lang="en">
<head>
<meta charset="utf-8">
<title>Kelson Coatworks — Business Card</title>
<link rel="stylesheet" href="https://fonts.googleapis.com/css2?family=Poppins:wght@400;500;800&display=swap">
<style>
  :root {
    --stage-top: #5a5a5a;
    --stage-bottom: #2e2e2e;
    --card: #1c1c1c;
    --card-edge: #141414;
    --ink: #ffffff;
    --ink-soft: #e6e6e6;
    --pattern-dark: #161616;
    --pattern-light: #3a3a3a;
  }
  * { box-sizing: border-box; margin: 0; padding: 0; }
  html, body { width: 1200px; height: 675px; overflow: hidden; }
  body {
    background: radial-gradient(ellipse at 50% 45%, var(--stage-top), var(--stage-bottom));
    font-family: "Poppins", sans-serif;
    color: var(--ink);
  }
  .stage {
    position: relative;
    width: 1200px; height: 675px;
    display: flex; align-items: center; justify-content: center; gap: 44px;
  }
  .card {
    position: relative;
    width: 520px; height: 297px;
    background: var(--card);
    border-radius: 4px;
    box-shadow: 0 18px 40px rgba(0,0,0,.45), 0 0 0 1px var(--card-edge);
    overflow: hidden;
  }
  /* front */
  .card-front__pattern {
    position: absolute; inset: 0;
    background: linear-gradient(100deg, var(--pattern-dark) 0%, var(--pattern-dark) 35%, var(--pattern-light) 75%, #262626 100%);
  }
  .card-front__brand {
    position: absolute; inset: 0;
    display: flex; align-items: center; justify-content: center; gap: 12px;
  }
  .brand-mark {
    width: 16px; height: 16px; background: var(--ink);
  }
  .brand-name {
    font-weight: 800; font-size: 32px; letter-spacing: .5px; text-transform: uppercase;
    color: var(--ink); line-height: 1;
  }
  /* back */
  .card-back { display: flex; align-items: center; }
  .card-back__brand {
    width: 270px; display: flex; align-items: center; justify-content: center; gap: 10px;
  }
  .card-back__brand .brand-name { font-size: 27px; }
  .card-back__brand .brand-mark { width: 13px; height: 13px; }
  .card-back__divider {
    width: 2px; height: 150px; background: var(--ink);
  }
  .contact {
    padding-left: 26px;
    font-size: 12px; line-height: 1.42; color: var(--ink-soft);
  }
  .contact__name { font-weight: 800; font-size: 17px; color: var(--ink); text-transform: uppercase; line-height: 1.2; }
  .contact__title { margin-bottom: 1px; }
  .contact__list { list-style: none; margin-top: 2px; }
  .contact__list li { display: flex; align-items: center; gap: 7px; letter-spacing: .3px; }
  .contact__list svg { width: 11px; height: 11px; flex: none; fill: var(--ink); }
</style>
</head>
<body>
<main class="stage">
  <section class="card card-front">
    <div class="card-front__pattern" role="img" aria-label="Faint repeated brand pattern across the card face"></div>
    <div class="card-front__brand">
      <span class="brand-mark"></span>
      <span class="brand-name">Kelson Coatworks</span>
    </div>
  </section>

  <section class="card card-back">
    <div class="card-back__brand">
      <span class="brand-mark"></span>
      <span class="brand-name">Kelson<br>Coatworks</span>
    </div>
    <div class="card-back__divider"></div>
    <div class="contact">
      <p class="contact__name">Dale Pickett</p>
      <p class="contact__title">Manager</p>
      <p class="contact__address">7-4417 Larchmere Avenue,<br>Abbotsford, BC, V3K 2R9</p>
      <ul class="contact__list">
        <li>604-555-0172</li>
        <li>
          <svg viewBox="0 0 24 24" aria-hidden="true"><path d="M6.6 10.8a15.1 15.1 0 0 0 6.6 6.6l2.2-2.2a1 1 0 0 1 1-.25 11.4 11.4 0 0 0 3.6.57 1 1 0 0 1 1 1V20a1 1 0 0 1-1 1A17 17 0 0 1 3 4a1 1 0 0 1 1-1h3.5a1 1 0 0 1 1 1c0 1.25.2 2.45.57 3.57a1 1 0 0 1-.25 1z"/></svg>
          604-555-0138
        </li>
        <li>
          <svg viewBox="0 0 24 24" aria-hidden="true"><path d="M2 5h20v14H2z M2 5l10 8 10-8" fill="none" stroke="#fff" stroke-width="2.4"/></svg>
          dale@kelsoncoatworks.ca
        </li>
        <li>
          <svg viewBox="0 0 24 24" aria-hidden="true"><circle cx="12" cy="12" r="9.5" fill="none" stroke="#fff" stroke-width="2.2"/><path d="M2.5 12h19M12 2.5c3 3 3 16 0 19M12 2.5c-3 3-3 16 0 19" fill="none" stroke="#fff" stroke-width="1.8"/></svg>
          www.kelsoncoatworks.ca
        </li>
      </ul>
    </div>
  </section>
</main>
</body>
</html>
```